Erstellung einer Sidebar auf Produktdetailseite
Zielgruppe
Wir sind spezialisiert auf den Import und Versand von italienischen Weinen. Unsere Zielgruppe sind Privatkunden.
Aufgabenstellung
Vorgabe: Erstellung einer Sidebar auf Produktdetailseite:
Wir möchten gezielt Neukunden auf Produktdetailseite z.B.
https://www.varlomedo.de/castello_ombrusa_weindetail/6757/Saverno-lXLII-Primitivo-di-Manduria-DOP
eine Sidebar unten rechts einblenden (auf dem holzfarbenen Hintergrund).
Wichtig ist, dass die Sidebar perfekt zum Stil unseres Online-Shops passt.
Format:
Ca. 200 Pixel breit und max 320 Pixel hoch
Inhalt: 3% als Grafik und Bild des Kellnermessers
Text:
Neukundenvorteil: 3% Rabatt & Kellnermesser gratis
Gutscheincode: Girasole42
*Gültig ab einem Mindestbestellwert von 70€ und nur für Neukunden.
Ziel:
Graphik soll den Kunden Willkommen heißen und zur Bestellung motivieren.

```html
<!DOCTYPE html>
<html lang="de">
<head>
<meta charset="utf-8">
<title>Neukundenvorteil Sidebar</title>
<link rel="stylesheet" href="https://fonts.googleapis.com/css2?family=Merriweather:wght@400;700&family=Source+Sans+3:wght@400;600;700&display=swap">
<style>
  :root {
    --wood-light: #d9c8b1;
    --wood-mid: #c9b195;
    --wood-dark: #b89d80;
    --card: #ffffff;
    --wine: #a3173e;
    --wine-deep: #8e1235;
    --ink: #111111;
    --knife-tone: #2a2a2a;
    --knife-bg: #f3f3f3;
  }
  * { box-sizing: border-box; margin: 0; padding: 0; }
  html, body { width: 943px; height: 1200px; overflow: hidden; }
  body { position: relative; font-family: "Source Sans 3", Arial, sans-serif; }

  .wood-backdrop {
    position: absolute; inset: 0;
    background: linear-gradient(100deg, var(--wood-mid) 0%, var(--wood-light) 45%, var(--wood-mid) 75%, var(--wood-dark) 100%);
  }

  .offer-card {
    position: absolute; left: 205px; top: 205px;
    width: 533px; height: 864px;
    background: var(--card);
    border-radius: 22px;
    overflow: hidden;
  }

  .offer-eyebrow {
    position: absolute; top: 228px; left: 0; right: 0;
    top: 22px;
    text-align: center;
    color: var(--wine);
    font-weight: 700;
    font-size: 47px;
    letter-spacing: 0.3px;
  }

  .offer-band {
    position: absolute; left: 0; right: 0; top: 92px; height: 210px;
    background: var(--wine);
    color: #fff;
    text-align: center;
  }
  .offer-headline {
    font-family: "Merriweather", Georgia, serif;
    font-size: 76px; line-height: 1;
    padding-top: 22px;
    font-weight: 400;
  }
  .offer-subline {
    font-family: "Merriweather", Georgia, serif;
    font-size: 44px; line-height: 1; margin-top: 8px;
  }
  .offer-code {
    font-size: 30px; font-weight: 600; margin-top: 18px;
  }

  .knife-visual {
    position: absolute; left: 26px; top: 339px; width: 478px; height: 349px;
    background: radial-gradient(ellipse at 50% 50%, var(--knife-tone) 0%, #555 45%, var(--knife-bg) 75%);
    border-radius: 12px;
  }

  .gratis-badge {
    position: absolute; left: 228px; top: 599px; width: 292px; height: 80px;
    background: var(--wine);
    color: #fff;
    font-weight: 700; font-size: 56px; letter-spacing: 1px;
    display: flex; align-items: center; justify-content: center;
  }

  .offer-terms {
    position: absolute; left: 52px; right: 30px; top: 737px;
    color: var(--ink);
    font-size: 29px; line-height: 42px;
  }
  .offer-terms strong { font-weight: 700; }
</style>
</head>
<body>
  <div class="wood-backdrop" role="img" aria-label="Holzmaserung als Hintergrund"></div>

  <aside class="offer-card">
    <h2 class="offer-eyebrow">Neukundenvorteil:</h2>

    <div class="offer-band">
      <p class="offer-headline">3% Rabatt</p>
      <p class="offer-subline">und Kellnermesser</p>
      <p class="offer-code">*Gutscheincode: Girasole42</p>
    </div>

    <div class="knife-visual" role="img" aria-label="Schwarzes Kellnermesser mit ausgeklapptem Korkenzieher"></div>

    <div class="gratis-badge">GRATIS</div>

    <p class="offer-terms"><strong>*Gültig ab</strong> einem Mindestbestellwert von <strong>70€</strong> und nur für Neukunden</p>
  </aside>
</body>
</html>
```